Redesign my business cards

I would like pretty much all the same information as my current business cards but redesigned to stand out more and be more unique photo uploaded to show my current business cards don’t mind if you want to remove or replace I for on the back

```html
<!DOCTYPE html>
<html lang="en">
<head>
<meta charset="utf-8">
<title>Vantor Detailing – Business Card</title>
<link href="https://fonts.googleapis.com/css2?family=Exo+2:wght@600;700&family=Roboto:wght@400;900&display=swap" rel="stylesheet">
<style>
  :root {
    --backdrop: #2b2b2b;
    --card-deep: #0b1a28;
    --card-mid: #13283b;
    --price-blue: #1e9fdc;
    --heading-grey: #d9dde2;
    --body-grey: #c6ccd3;
    --rule-teal: #3b8fb0;
    --band-teal: #68bccf;
    --ink-navy: #0d1e2d;
    --brand-blue: #4e8fd6;
    --brand-ring: #2f6fb8;
  }
  * { box-sizing: border-box; margin: 0; padding: 0; }
  html, body { width: 1200px; height: 1138px; overflow: hidden; }
  body { background: var(--backdrop); position: relative; font-family: "Roboto", sans-serif; }

  .card {
    position: absolute;
    border-radius: 16px;
    overflow: hidden;
    background: linear-gradient(160deg, var(--card-mid) 0%, var(--card-deep) 100%);
    box-shadow: 0 6px 14px rgba(0,0,0,0.45);
  }
  .card--services { left: 274px; top: 186px; width: 623px; height: 376px; }
  .card--contact  { left: 276px; top: 608px; width: 618px; height: 374px; background: var(--card-deep); }

  .backdrop-art {
    position: absolute; left: 300px; top: 0; width: 323px; height: 376px;
    background: radial-gradient(ellipse at 60% 40%, rgba(40,90,125,0.35) 0%, rgba(20,50,75,0.12) 60%, rgba(0,0,0,0) 80%);
  }

  .service { position: absolute; left: 21px; }
  .service__title {
    font-family: "Exo 2", sans-serif; font-weight: 700; font-size: 22px;
    color: var(--heading-grey); letter-spacing: 0.2px; line-height: 28px; white-space: nowrap;
  }
  .service__price { color: var(--price-blue); font-size: 28px; margin-left: 10px; }
  .service__desc { font-size: 15px; line-height: 19px; color: var(--body-grey); margin-top: 4px; }
  .service--interior { top: 38px; width: 590px; }
  .service--exterior { top: 133px; width: 590px; }
  .service--full { top: 228px; width: 425px; }
  .service--full .service__desc { text-align: justify; }

  .rule { position: absolute; left: 21px; height: 1px; background: var(--rule-teal); }
  .rule--one { top: 122px; width: 582px; }
  .rule--two { top: 218px; width: 431px; }

  .brand-mini { position: absolute; left: 440px; top: 205px; width: 165px; text-align: center; }
  .brand-mini__dot { width: 92px; height: 92px; border-radius: 50%; background: var(--brand-ring); margin: 0 auto 8px; }
  .brand-mini__name {
    font-family: "Exo 2", sans-serif; font-weight: 700; font-size: 19px; line-height: 20px;
    color: var(--brand-blue); letter-spacing: 1px; text-transform: uppercase;
  }

  .brand { position: absolute; left: 88px; top: 44px; display: flex; align-items: center; gap: 16px; }
  .brand__dot { width: 128px; height: 128px; border-radius: 50%; background: var(--brand-ring); flex: none; }
  .brand__name {
    font-family: "Exo 2", sans-serif; font-weight: 700; font-size: 46px; line-height: 48px;
    color: var(--brand-blue); letter-spacing: 2px; text-transform: uppercase;
  }

  .contact-band {
    position: absolute; left: 0; top: 213px; width: 100%; height: 97px;
    background: var(--band-teal); color: var(--ink-navy); text-align: center;
  }
  .contact-band__name { margin-top: 14px; white-space: nowrap; }
  .person { font-family: "Exo 2", sans-serif; font-weight: 700; font-size: 31px; vertical-align: middle; }
  .role { font-size: 16px; vertical-align: middle; margin-left: 6px; }
  .phone { font-weight: 900; font-size: 32px; margin-top: 2px; display: flex; justify-content: center; align-items: center; gap: 14px; }
  .phone svg { width: 22px; height: 22px; }

  .email {
    position: absolute; left: 0; top: 324px; width: 100%;
    display: flex; justify-content: center; align-items: center; gap: 12px;
    color: var(--body-grey); font-size: 17px;
  }
  .email svg { width: 16px; height: 12px; }
</style>
</head>
<body>

<section class="card card--services">
  <div class="backdrop-art" role="img" aria-label="Faint large car illustration in the background"></div>

  <div class="service service--interior">
    <h2 class="service__title">INTERIOR DETAIL<span class="service__price">$150</span></h2>
    <p class="service__desc">Vacume &amp; Deep clean of carpets &amp; upholstery or leather treatment, interior trim clean &amp; condition, window polish and treatment, steam clean &amp; stain removal</p>
  </div>
  <div class="rule rule--one"></div>

  <div class="service service--exterior">
    <h2 class="service__title">EXTERIOR DETAIL<span class="service__price">$250</span></h2>
    <p class="service__desc">Extreme wash &amp; polish, exterior trim reviver &amp; protector window polish &amp; treatment, tyre dressing, engine bay cleaned</p>
  </div>
  <div class="rule rule--two"></div>

  <div class="service service--full">
    <h2 class="service__title">FULL EXTREME DETAILS<span class="service__price">$350</span></h2>
    <p class="service__desc">Extreme wash and polish, tyre dressing, engine bay cleaned, vacume &amp; deep clean of carpets &amp; upholstery or leather treatment, interior &amp; exterior trim reviver &amp; protector, window polish and treatment</p>
  </div>

  <div class="brand-mini">
    <div class="brand-mini__dot"></div>
    <div class="brand-mini__name">Vantor<br>Detailing</div>
  </div>
</section>

<section class="card card--contact">
  <div class="brand">
    <div class="brand__dot"></div>
    <div class="brand__name">Vantor<br>Detailing</div>
  </div>

  <div class="contact-band">
    <p class="contact-band__name"><span class="person">Dane Holloway</span><span class="role">| Owner/Operator</span></p>
    <p class="phone">
      <svg viewBox="0 0 24 24" aria-hidden="true"><path fill="#0d1e2d" d="M2 9c0-3 5-5 10-5s10 2 10 5v2h-5V8.5c-1.5-.6-3.2-.9-5-.9s-3.5.3-5 .9V11H2zM6 12l2-3h8l2 3 2 8H4zm6 2a2.5 2.5 0 100 5 2.5 2.5 0 000-5z"/></svg>
      0455123670
    </p>
  </div>

  <p class="email">
    <svg viewBox="0 0 16 12" aria-hidden="true"><rect x="0.5" y="0.5" width="15" height="11" fill="none" stroke="#c6ccd3"/><path d="M0.5 0.5L8 7l7.5-6.5M0.5 11.5L6 6M15.5 11.5L10 6" fill="none" stroke="#c6ccd3"/></svg>
    vantordetailing@example.com
  </p>
</section>

</body>
</html>
```